120ml Jar Label — Masculine Cosmetic Foot Balm for Cracked, Hardworking Heels

We need a print-ready wraparound label for a 120ml jar — a brown/amber glass jar with a black metal screw lid (file photo attached).

--DO NOT PUT A BARCODE ON THE LABEL PLEASE--
**PLEASE READ "PIXEL HARBOUR PROJECT BRIEF FINAL.MD" IN ATTACHED FILES IF YOU ARE SUBMITTING A DESIGN.**

The label is 190mm wide × 40mm high.
We need files to be in an .ai format with a 2mm bleed at the end.
Social media handle: @tallowgatenz (facebook, instagram and tiktok)

Tallow Gate is a New Zealand foot-care brand making practical, no-nonsense products for hardworking men whose jobs wreck their feet. Our flagship product, Ridge Mender Balm, helps fix thick, cracked, hardworking skin.

Brand color scheme and overview is all in the brief file. You may add some brand aligned colors outside of the specified hex codes as you see fit to make a great design. Feel free to remove the "Tallow Gate" text from the logo so Tallow Gate is not doubled up on the front of the label

The tone we want: direct, rugged, and credible — like a workwear brand, not a spa brand. Most cracked-heel products on the market lean soft and feminine; we want to stand apart by looking like a serious fix for a real problem, made in New Zealand.

Full legal requirements for New Zealand cosmetic labelling (ingredients, directions, net contents, origin, etc.) are listed in the attached brief document — these are non-negotiable and must stay legible.

Please see the label attached "Label spacing guide" for this project's rough spacing guide. This label is the same size and sits well on the jar. This label doesn't need to be spaced quite as much as the Brisko Label

I want to run the design for a week - I feel 7 days is a good amount of time for designers to see the work, digest the brief and create something remarkable and memorable for Tallow Gate.

Target Market(s)

Working men in New Zealand whose jobs or lifestyle put heavy wear on their feet — tradies, farmers, hospital/shift workers, hunters, and outdoors people. Practical, value-driven buyers rather than luxury skincare shoppers.

Industry/Entity Type

Beauty / Health & Wellness / Cosmetics

Font styles to use
Sans Serif
Other font styles liked:
• Montserrat (bold, headings), Inter (regular, body)

Colors
00AB8E
00BBA5
67D7C9
C6EFE9
E9F9F6
FFC000
F8CF3A
FAE287
FDF2CF
FEFAEE

Requirements
Must have
• All NZ cosmetic labelling requirements from the attached brief (product name, tag line, net contents, ingredients, directions, storage, made in NZ) — legible and complete, not omitted for aesthetics Fits 190mm × 40mm wraparound format for a 120ml brown jar with black lid Uses our existing brand colors: Deep Olive #3C4A34, Bone White #F4EFE6, Terracotta Clay #C1683D, and Warm Grey #4A4540 (exact palette in attached brief) Uses Montserrat (headings) and Inter (body) or close equivalents Incorporates our existing shield-and-wing logo (attached) Brand name and product name clearly readable from a normal shelf/bathroom-cabinet distance
Nice to have
• A style that could extend into a hero/product photo later, similar to the NZ-hills-backdrop look on our website (screenshot attached) — not required for the label itself, just good to keep in mind Original icon work (e.g. a small soak/apply/sock icon set) if it fits the rugged brand feel A design that could work as a small back-label/wraparound split if the front can't fit everything at a readable size
Should not have
• No pastel colors, floral motifs, or delicate script fonts — this should never look like spa/luxury skincare. Don't introduce new brand colors outside the palette provided other than black.

```html
<!DOCTYPE html>
<html lang="en">
<head>
<meta charset="utf-8">
<title>Tallow Gate – Ridge Mender Balm label options</title>
<link rel="stylesheet" href="https://fonts.googleapis.com/css2?family=Inter:wght@400;600&family=Montserrat:wght@700;800;900&display=swap">
<style>
:root{
  --stage:#9c9ca6;
  --olive-deep:#1e3a2f;
  --saddle:#8b5a2b;
  --clay:#c1683d;
  --bone:#f3efe6;
  --sand:#f5e4c6;
  --cream-ink:#f4e6c8;
  --ink:#2e2a26;
  --number:#111;
}
*{box-sizing:border-box;margin:0;padding:0}
html,body{width:1200px;height:1035px;overflow:hidden}
body{background:var(--stage);position:relative;font-family:"Inter",sans-serif;color:var(--ink)}

.option-number{position:absolute;left:72px;width:44px;text-align:center;font-family:"Inter",sans-serif;font-size:60px;line-height:1;color:var(--number)}

.label{
  position:absolute;left:156px;width:968px;height:203px;border-radius:12px;overflow:hidden;
  display:grid;grid-template-columns:1fr 386px 1fr;
  --inset:0px;--side-bg:var(--bone);--side-ink:var(--ink);--accent:var(--saddle);--icon:var(--saddle);
}
.label--framed{border:8px solid var(--saddle);--inset:8px}
.label--saddle{--side-bg:var(--saddle);--side-ink:var(--cream-ink);--accent:var(--cream-ink);--icon:var(--cream-ink)}
.label--sand{--side-bg:var(--sand)}

.panel{position:relative;height:100%}
.panel--side{background:var(--side-bg);color:var(--side-ink)}
.panel--front{background:var(--olive-deep);color:var(--cream-ink)}
.panel>*{position:absolute}

.body-copy{font-size:11.3px;line-height:12.4px;width:250px}
.body-copy b{color:var(--accent);font-weight:600}
.storage{left:calc(27px - var(--inset));top:calc(28px - var(--inset))}
.rule{left:calc(27px - var(--inset));top:calc(64px - var(--inset));width:240px;height:1px;background:var(--accent)}
.ingredients{left:calc(27px - var(--inset));top:calc(72px - var(--inset))}
.sign-off{left:calc(27px - var(--inset));top:calc(157px - var(--inset));font-size:11.3px;line-height:12.4px;text-transform:uppercase}
.sign-off b{display:block;color:var(--accent);font-weight:600}
.social{left:calc(150px - var(--inset));top:calc(163px - var(--inset));display:flex;align-items:center;gap:6px;font-size:11.3px}
.social-dot{width:9px;height:9px;border-radius:50%;background:var(--side-ink)}

.brand{left:0;right:0;top:calc(16px - var(--inset));display:flex;justify-content:center;align-items:center;gap:10px}
.brand-mark{width:42px;height:46px;border-radius:6px;background:linear-gradient(160deg,#c1683d,#8b5a2b)}
.brand-name{font-family:"Montserrat",sans-serif;font-weight:900;font-size:22px;line-height:22px;color:var(--cream-ink);letter-spacing:.3px}
.product-name{left:0;right:0;top:calc(73px - var(--inset));text-align:center;font-family:"Montserrat",sans-serif;font-weight:900;font-size:34px;line-height:33px;color:var(--cream-ink)}
.tagline{left:50%;transform:translateX(-50%);top:calc(146px - var(--inset));width:153px;height:16px;border-radius:8px;background:var(--clay);color:var(--cream-ink);font-size:11px;line-height:16px;text-align:center;letter-spacing:.3px}
.net{left:46px;top:calc(177px - var(--inset));font-size:9.5px;letter-spacing:.3px}
.origin{left:272px;top:calc(164px - var(--inset));width:68px;height:23px;border:1.5px solid var(--cream-ink);text-align:center;font-family:"Montserrat",sans-serif}
.origin span{display:block;font-weight:800;font-size:11px;line-height:12px}
.origin small{display:block;background:var(--cream-ink);color:var(--olive-deep);font-weight:700;font-size:6px;line-height:8px;letter-spacing:1.3px}

.directions-title{left:96px;top:calc(6px - var(--inset));font-weight:600;font-size:13px;color:var(--accent)}
.icon{left:26px;width:30px;height:30px;border-radius:6px;background:var(--icon);opacity:.9}
.step{left:72px;width:200px;font-size:11px;line-height:12.4px}
.small-mark{width:18px;height:18px;border-radius:4px;background:var(--icon);top:calc(166px - var(--inset))}
</style>
</head>
<body>

<div class="option-number" style="top:132px">1</div>
<div class="option-number" style="top:369px">2</div>
<div class="option-number" style="top:601px">3</div>
<div class="option-number" style="top:845px">4</div>

<!-- option 1 -->
<section class="label label--framed" style="top:59px">
  <div class="panel panel--side">
    <p class="body-copy storage"><b>STORAGE:</b> Keep out of direct sunlight. Best used within six months of opening.</p>
    <div class="rule"></div>
    <p class="body-copy ingredients"><b>INGREDIENTS:</b> Shea Butter, Beef Tallow, Beeswax, Grape Seed Oil, Vegetable Glycerin, Lanolin, Panthenol, Gluconolactone, Sodium Benzoate, Allantoin, Manuka Honey, Vitamin E, Tea Tree Essential Oil, Lemon Myrtle Essential Oil, Rosemary Oleoresin Extract.</p>
    <p class="sign-off"><b>Getting you back</b>On your feet</p>
    <p class="social"><span class="social-dot"></span>@tallowgatenz</p>
  </div>
  <div class="panel panel--front">
    <div class="brand"><div class="brand-mark" role="img" aria-label="Tallow Gate shield emblem"></div><p class="brand-name">TALLOW GATE<br>NZ</p></div>
    <h2 class="product-name">RIDGE MENDER<br>BALM</h2>
    <p class="tagline">For Hardworking Soles</p>
    <p class="net">40 oz / 120ml</p>
    <p class="origin"><span>MADE IN</span><small>NEW ZEALAND</small></p>
  </div>
  <div class="panel panel--side">
    <h3 class="directions-title">DIRECTIONS:</h3>
    <div class="icon" style="top:calc(27px - var(--inset))" role="img" aria-label="Balm jar icon"></div>
    <p class="step" style="top:calc(34px - var(--inset))">Apply generously.</p>
    <div class="icon" style="top:calc(66px - var(--inset))" role="img" aria-label="Clean foot icon"></div>
    <p class="step" style="top:calc(70px - var(--inset))">To clean, dry feet, focusing on heels and thick or cracked areas.</p>
    <div class="icon" style="top:calc(110px - var(--inset))" role="img" aria-label="Socks at night icon"></div>
    <p class="step" style="top:calc(113px - var(--inset))">For cracked heels, wear our moisture-locking socks overnight.</p>
    <div class="icon" style="top:calc(153px - var(--inset))" role="img" aria-label="Daily calendar icon"></div>
    <p class="step" style="top:calc(162px - var(--inset))">Use daily.</p>
    <div class="small-mark" style="left:207px" role="img" aria-label="Recycling code 5"></div>
    <div class="small-mark" style="left:242px" role="img" aria-label="Use within 6 months after opening"></div>
  </div>
</section>

<!-- option 2 -->
<section class="label label--saddle" style="top:296px">
  <div class="panel panel--side">
    <p class="body-copy storage"><b>STORAGE:</b> Keep out of direct sunlight. Best used within six months of opening.</p>
    <div class="rule"></div>
    <p class="body-copy ingredients"><b>INGREDIENTS:</b> Shea Butter, Beef Tallow, Beeswax, Grape Seed Oil, Vegetable Glycerin, Lanolin, Panthenol, Gluconolactone, Sodium Benzoate, Allantoin, Manuka Honey, Vitamin E, Tea Tree Essential Oil, Lemon Myrtle Essential Oil, Rosemary Oleoresin Extract.</p>
    <p class="sign-off"><b>Getting you back</b>On your feet</p>
    <p class="social"><span class="social-dot"></span>@tallowgatenz</p>
  </div>
  <div class="panel panel--front">
    <div class="brand"><div class="brand-mark" role="img" aria-label="Tallow Gate shield emblem"></div><p class="brand-name">TALLOW GATE<br>NZ</p></div>
    <h2 class="product-name">RIDGE MENDER<br>BALM</h2>
    <p class="tagline">For Hardworking Soles</p>
    <p class="net">40 oz / 120ml</p>
    <p class="origin"><span>MADE IN</span><small>NEW ZEALAND</small></p>
  </div>
  <div class="panel panel--side">
    <h3 class="directions-title" style="left:107px">DIRECTIONS:</h3>
    <div class="icon" style="top:27px" role="img" aria-label="Balm jar icon"></div>
    <p class="step" style="top:34px">Apply generously.</p>
    <div class="icon" style="top:66px" role="img" aria-label="Clean foot icon"></div>
    <p class="step" style="top:70px">To clean, dry feet, focusing on heels and thick or cracked areas.</p>
    <div class="icon" style="top:110px" role="img" aria-label="Socks at night icon"></div>
    <p class="step" style="top:113px">For cracked heels, wear our moisture-locking socks overnight.</p>
    <div class="icon" style="top:153px" role="img" aria-label="Daily calendar icon"></div>
    <p class="step" style="top:162px">Use daily.</p>
    <div class="small-mark" style="left:226px" role="img" aria-label="Recycling code 5"></div>
    <div class="small-mark" style="left:261px" role="img" aria-label="Use within 6 months after opening"></div>
  </div>
</section>

<!-- option 3 -->
<section class="label" style="top:528px">
  <div class="panel panel--side">
    <p class="body-copy storage"><b>STORAGE:</b> Keep out of direct sunlight. Best used within six months of opening.</p>
    <div class="rule"></div>
    <p class="body-copy ingredients"><b>INGREDIENTS:</b> Shea Butter, Beef Tallow, Beeswax, Grape Seed Oil, Vegetable Glycerin, Lanolin, Panthenol, Gluconolactone, Sodium Benzoate, Allantoin, Manuka Honey, Vitamin E, Tea Tree Essential Oil, Lemon Myrtle Essential Oil, Rosemary Oleoresin Extract.</p>
    <p class="sign-off"><b>Getting you back</b>On your feet</p>
    <p class="social"><span class="social-dot"></span>@tallowgatenz</p>
  </div>
  <div class="panel panel--front">
    <div class="brand"><div class="brand-mark" role="img" aria-label="Tallow Gate shield emblem"></div><p class="brand-name">TALLOW GATE<br>NZ</p></div>
    <h2 class="product-name">RIDGE MENDER<br>BALM</h2>
    <p class="tagline">For Hardworking Soles</p>
    <p class="net">40 oz / 120ml</p>
    <p class="origin"><span>MADE IN</span><small>NEW ZEALAND</small></p>
  </div>
  <div class="panel panel--side">
    <h3 class="directions-title">DIRECTIONS:</h3>
    <div class="icon" style="top:27px" role="img" aria-label="Balm jar icon"></div>
    <p class="step" style="top:34px">Apply generously.</p>
    <div class="icon" style="top:66px" role="img" aria-label="Clean foot icon"></div>
    <p class="step" style="top:70px">To clean, dry feet, focusing on heels and thick or cracked areas.</p>
    <div class="icon" style="top:110px" role="img" aria-label="Socks at night icon"></div>
    <p class="step" style="top:113px">For cracked heels, wear our moisture-locking socks overnight.</p>
    <div class="icon" style="top:153px" role="img" aria-label="Daily calendar icon"></div>
    <p class="step" style="top:162px">Use daily.</p>
    <div class="small-mark" style="left:207px" role="img" aria-label="Recycling code 5"></div>
    <div class="small-mark" style="left:242px" role="img" aria-label="Use within 6 months after opening"></div>
  </div>
</section>

<!-- option 4 -->
<section class="label label--sand" style="top:772px">
  <div class="panel panel--side">
    <p class="body-copy storage"><b>STORAGE:</b> Keep out of direct sunlight. Best used within six months of opening.</p>
    <div class="rule"></div>
    <p class="body-copy ingredients"><b>INGREDIENTS:</b> Shea Butter, Beef Tallow, Beeswax, Grape Seed Oil, Vegetable Glycerin, Lanolin, Panthenol, Gluconolactone, Sodium Benzoate, Allantoin, Manuka Honey, Vitamin E, Tea Tree Essential Oil, Lemon Myrtle Essential Oil, Rosemary Oleoresin Extract.</p>
    <p class="sign-off"><b>Getting you back</b>On your feet</p>
    <p class="social"><span class="social-dot"></span>@tallowgatenz</p>
  </div>
  <div class="panel panel--front">
    <div class="brand"><div class="brand-mark" role="img" aria-label="Tallow Gate shield emblem"></div><p class="brand-name">TALLOW GATE<br>NZ</p></div>
    <h2 class="product-name">RIDGE MENDER<br>BALM</h2>
    <p class="tagline">For Hardworking Soles</p>
    <p class="net">40 oz / 120ml</p>
    <p class="origin"><span>MADE IN</span><small>NEW ZEALAND</small></p>
  </div>
  <div class="panel panel--side">
    <h3 class="directions-title">DIRECTIONS:</h3>
    <div class="icon" style="top:27px" role="img" aria-label="Balm jar icon"></div>
    <p class="step" style="top:34px">Apply generously.</p>
    <div class="icon" style="top:66px" role="img" aria-label="Clean foot icon"></div>
    <p class="step" style="top:70px">To clean, dry feet, focusing on heels and thick or cracked areas.</p>
    <div class="icon" style="top:110px" role="img" aria-label="Socks at night icon"></div>
    <p class="step" style="top:113px">For cracked heels, wear our moisture-locking socks overnight.</p>
    <div class="icon" style="top:153px" role="img" aria-label="Daily calendar icon"></div>
    <p class="step" style="top:162px">Use daily.</p>
    <div class="small-mark" style="left:207px" role="img" aria-label="Recycling code 5"></div>
    <div class="small-mark" style="left:242px" role="img" aria-label="Use within 6 months after opening"></div>
  </div>
</section>

</body>
</html>
```